GHollis Busisness Card

I am an aerospace consultant and at this time only need business cards.

Industry/Entity Type

Business

Contact Information for Business Card

Hollis Partners,LLC
Gerald T. Hollis

348 Birch Hollow Road
Madison AL 35762

256-555-0148 (cell)
256-555-0173 (fax)

geraldhollis@mailbrook.net

```html
<!DOCTYPE html>
<html lang="en">
<head>
<meta charset="UTF-8">
<title>Hollis Partners LLC — Business Card</title>
<link rel="stylesheet" href="https://fonts.googleapis.com/css2?family=Montserrat:wght@400;500;600;700&display=swap">
<style>
  :root {
    --backdrop: #e8e6e1;
    --navy-deep: #0b1627;
    --navy-mid: #1c375a;
    --ink: #182a45;
    --band-light: #ffffff;
    --band-shade: #e4e4e4;
    --paper-text: #dfe6ef;
    --line: rgba(255,255,255,0.85);
  }
  * { box-sizing: border-box; margin: 0; padding: 0; }
  html, body {
    width: 1200px; height: 800px; overflow: hidden;
    background: var(--backdrop);
    font-family: "Montserrat", sans-serif;
  }
  .sheet {
    width: 1200px; height: 800px;
    display: flex; flex-direction: column;
    align-items: center; justify-content: center; gap: 40px;
  }
  .card {
    position: relative;
    width: 620px; height: 354px;
    overflow: hidden;
    background: radial-gradient(ellipse at 55% 45%, var(--navy-mid) 0%, var(--navy-deep) 75%);
    box-shadow: 0 6px 18px rgba(0,0,0,0.18);
  }
  .band {
    position: absolute; left: 0; right: 0;
    background: linear-gradient(100deg, var(--band-shade) 0%, var(--band-light) 45%, var(--band-shade) 100%);
    display: flex; flex-direction: column; align-items: center; justify-content: center;
    color: var(--ink);
  }
  .card--front .band { top: 36%; height: 52%; }
  .card--back .band { top: 0; height: 50%; padding-top: 10px; }
  .brand-name {
    font-weight: 600; font-size: 40px; line-height: 1; letter-spacing: 0.5px;
  }
  .brand-suffix {
    font-weight: 600; font-size: 22px; margin-top: 6px; letter-spacing: 0.5px;
  }
  .strokes { position: absolute; }
  .contact-row {
    position: absolute; left: 0; right: 0; top: 58%; bottom: 0;
    display: grid; grid-template-columns: 1fr 1.2fr 1fr 1.2fr;
    padding: 0 18px;
  }
  .contact {
    display: flex; flex-direction: column; align-items: center;
    gap: 14px; padding-top: 14px;
    color: var(--paper-text); font-size: 11px; text-align: center; line-height: 1.45;
    letter-spacing: 0.3px;
  }
  .contact:nth-child(1) { padding-top: 40px; }
  .contact:nth-child(2) { padding-top: 26px; }
  .contact:nth-child(3) { padding-top: 8px; }
  .contact:nth-child(4) { padding-top: 0; }
  .icon-box { width: 26px; height: 26px; }
</style>
</head>
<body>
<main class="sheet">

  <section class="card card--front" aria-label="Card front">
    <svg class="strokes" style="right:36px; top:104px;" width="70" height="24" viewBox="0 0 70 24">
      <g stroke="var(--line)" stroke-width="1.3">
        <line x1="2" y1="4" x2="30" y2="22"/><line x1="26" y1="6" x2="46" y2="22"/><line x1="44" y1="8" x2="64" y2="22"/>
      </g>
    </svg>
    <div class="band">
      <span class="brand-name">Hollis</span>
      <span class="brand-suffix">Partners LLC</span>
    </div>
    <svg class="strokes" style="left:96px; top:296px;" width="40" height="38" viewBox="0 0 40 38">
      <g stroke="var(--line)" stroke-width="1.3">
        <line x1="4" y1="34" x2="10" y2="14"/><line x1="16" y1="34" x2="24" y2="4"/>
      </g>
    </svg>
  </section>

  <section class="card card--back" aria-label="Card back">
    <div class="band">
      <span class="brand-name">Hollis</span>
      <span class="brand-suffix">Partners LLC</span>
    </div>
    <svg class="strokes" style="right:54px; top:178px;" width="40" height="34" viewBox="0 0 40 34">
      <g stroke="var(--line)" stroke-width="1.3">
        <line x1="4" y1="32" x2="10" y2="4"/><line x1="16" y1="32" x2="22" y2="4"/><line x1="28" y1="32" x2="34" y2="4"/>
      </g>
    </svg>
    <svg class="strokes" style="left:106px; top:178px;" width="60" height="20" viewBox="0 0 60 20">
      <g stroke="var(--line)" stroke-width="1.3">
        <line x1="2" y1="2" x2="22" y2="16"/><line x1="20" y1="2" x2="40" y2="16"/><line x1="38" y1="2" x2="58" y2="16"/>
      </g>
    </svg>

    <div class="contact-row">
      <div class="contact contact--name">
        <svg class="icon-box" viewBox="0 0 26 26" aria-hidden="true">
          <rect x="1" y="1" width="24" height="24" fill="none" stroke="#fff" stroke-width="1.5"/>
          <circle cx="13" cy="10" r="3.5" fill="#fff"/>
          <path d="M6.5 20 Q13 12 19.5 20 Z" fill="#fff"/>
        </svg>
        <span>Gerald T. Hollis</span>
      </div>
      <div class="contact contact--address">
        <svg class="icon-box" viewBox="0 0 26 26" aria-hidden="true">
          <rect x="1" y="1" width="24" height="24" fill="none" stroke="#fff" stroke-width="1.5"/>
          <path d="M13 20 L8.5 12 A5 5 0 1 1 17.5 12 Z" fill="#fff"/>
          <circle cx="13" cy="10.5" r="1.8" fill="var(--navy-mid)"/>
        </svg>
        <span>348 Birch Hollow Road<br>Madison AL 35762</span>
      </div>
      <div class="contact contact--phone">
        <svg class="icon-box" viewBox="0 0 26 26" aria-hidden="true">
          <rect x="1" y="1" width="24" height="24" fill="none" stroke="#fff" stroke-width="1.5"/>
          <path d="M9 7 L11 7 L12 10 L10.6 11.2 Q12 14.2 14.8 15.4 L16 14 L19 15 L19 17 Q18.5 19 16.5 19 Q8.5 17.5 7 9.5 Q7 7.5 9 7 Z" fill="#fff"/>
        </svg>
        <span>256-555-0148<br>FAX: 256-555-0173</span>
      </div>
      <div class="contact contact--email">
        <svg class="icon-box" viewBox="0 0 26 26" aria-hidden="true">
          <rect x="1" y="1" width="24" height="24" fill="none" stroke="#fff" stroke-width="1.5"/>
          <rect x="7" y="9" width="12" height="8" fill="#fff"/>
          <path d="M7 9 L13 13.5 L19 9" fill="none" stroke="var(--navy-mid)" stroke-width="1.2"/>
        </svg>
        <span>geraldhollis@mailbrook.net</span>
      </div>
    </div>
  </section>

</main>
</body>
</html>
```